HVAC Company Business Card design with attached logo

Looking for an easily readable and attractive business card design that includes my attached company logo. I selected one sided card because it's more traditional, but I'm open to a 2-sided design. All of the details should be included in the design. Looking to create a professional, upscale image.

Target Market(s)

Commercial and residential consumers

Industry/Entity Type

Hvac

Contact Information for Business Card

Company phone number is 631.587.0293
Company email dennis@pinecresthvac.example
Company name is Silver Pine Air Conditioning, Refrigeration, and Heating
Dennis Harlow
Owner Operator
Company Address is
PO Box 872,
527 Maplewood Rd,
Fernwood, CT 11862
Business License K7158920000
Insured

Font styles to use
Serif
Sans Serif

Colors

Designer to choose colors to be used in the design.

Requirements
Must have
• Must include the logo.
Nice to have
• It seems like it should be a one sided card, but I'm open to a 2 sided one.

```html
<!DOCTYPE html>
<html lang="en">
<head>
<meta charset="utf-8">
<title>Silver Pine Business Card</title>
<link href="https://fonts.googleapis.com/css2?family=Arimo:wght@400;700&display=swap" rel="stylesheet">
<style>
  :root {
    --stage: #181818;
    --card: #ffffff;
    --brand-blue: #2b4aa0;
    --brand-orange: #f26a1e;
    --faint-grey: #e6e6e6;
  }
  html, body {
    margin: 0;
    padding: 0;
    width: 1200px;
    height: 856px;
    overflow: hidden;
    background: var(--stage);
    font-family: "Arimo", Arial, sans-serif;
  }
  .stage {
    position: relative;
    width: 1200px;
    height: 856px;
  }
  .card {
    position: absolute;
    left: 383px;
    width: 428px;
    height: 238px;
    background: var(--card);
    border-radius: 2px;
    overflow: hidden;
  }
  .card--front { top: 171px; }
  .card--back { top: 463px; }

  .contact {
    position: absolute;
    left: 35px;
    top: 0;
    color: var(--brand-blue);
  }
  .contact > * { position: absolute; left: 0; margin: 0; white-space: nowrap; }
  .address { top: 31px; font-size: 14px; line-height: 15px; }
  .person-name { top: 96px; font-size: 18.5px; font-weight: 400; }
  .person-role { top: 122px; font-size: 15px; font-weight: 700; }
  .phone { top: 145px; font-size: 16.5px; }
  .email { top: 166px; font-size: 16.5px; }
  .license { top: 207px; font-size: 14.5px; color: var(--brand-orange); }

  .watermark-name {
    position: absolute;
    right: 16px;
    top: 70px;
    font-size: 40px;
    line-height: 44px;
    font-weight: 700;
    color: var(--faint-grey);
    text-align: right;
  }

  .brand {
    position: absolute;
    left: 50%;
    top: 50%;
    transform: translate(-50%, -50%);
    display: flex;
    align-items: center;
    gap: 10px;
    white-space: nowrap;
  }
  .brand-dot {
    width: 22px;
    height: 22px;
    border-radius: 50%;
    background: var(--brand-orange);
  }
  .brand-name {
    font-size: 26px;
    font-weight: 700;
    color: var(--brand-blue);
  }
</style>
</head>
<body>
<main class="stage">
  <section class="card card--front" aria-label="Card front">
    <div class="watermark-name" aria-hidden="true">Silver<br>Pine</div>
    <div class="contact">
      <p class="address">PO Box 872<br>527 Maplewood Rd,<br>Fernwood, CT 11862,</p>
      <h1 class="person-name">Dennis Harlow</h1>
      <p class="person-role">Owner Operator</p>
      <p class="phone">631.587.0293</p>
      <p class="email">dennis@pinecresthvac.example</p>
      <p class="license">Business License K7158920000</p>
    </div>
  </section>

  <section class="card card--back" aria-label="Card back">
    <div class="brand">
      <span class="brand-dot"></span>
      <span class="brand-name">Silver Pine</span>
    </div>
  </section>
</main>
</body>
</html>
```